HR services to some of biggest Silicon Valley Tech companies needs a new website

We need a new website design probably 4-5 pages initially. Here are some websites we like the look of https://quintarimhub.com/ , https://www.mervoly.com/ and https://tavrine.com/ .
Updates

Slow in providing feedback

Target Market(s)

Silicon valley tech companies

Industry/Entity Type

HR

Coding

Coded - Design and coding required

Number of Pages Required

5+ page

Requirements
Nice to have
• any stock photos or images should show a diverse group of people. Our client base is very diverse

```html
<!DOCTYPE html>
<html lang="en">
<head>
<meta charset="utf-8">
<title>Tallo HR Consulting</title>
<link href="https://fonts.googleapis.com/css2?family=Poppins:wght@300;400;500;600&family=Rajdhani:wght@700&display=swap" rel="stylesheet">
<style>
:root{
  --yellow:#fcc31e;
  --dark:#232323;
  --darker:#1c1c1c;
  --ink:#1e1e1e;
  --muted:#6d6d6d;
  --light:#f7f7f7;
  --white:#ffffff;
}
*{margin:0;padding:0;box-sizing:border-box}
html,body{width:1200px;height:5017px;overflow:hidden}
body{font-family:"Poppins",sans-serif;color:var(--ink);background:var(--white);position:relative}
.section{position:absolute;left:0;width:1200px;overflow:hidden}
.accent{color:var(--yellow)}
.fill{position:absolute}

/* hero */
.hero{top:0;height:711px;background:var(--white)}
.hero-photo{left:0;top:0;width:1200px;height:711px;background:linear-gradient(120deg,#3b3a38 0%,#6b6864 45%,#8a8680 70%,#4e4c49 100%)}
.hero-shade{left:0;top:0;width:1200px;height:711px;background:rgba(20,20,20,.35)}
.hero-shape{position:absolute;left:0;top:0}
.brand{position:absolute;left:58px;top:66px;font-weight:500;font-size:18px;letter-spacing:1px;color:var(--white);display:flex;align-items:center;gap:10px}
.brand .mark{width:14px;height:14px;background:var(--yellow)}
.nav{position:absolute;top:36px;left:600px;display:flex;align-items:center;gap:22px;font-size:11.5px;color:var(--white)}
.nav .active{color:var(--yellow)}
.nav .cta{background:var(--yellow);color:var(--ink);font-weight:600;border-radius:20px;padding:10px 18px;margin-left:4px}
.hero-title{position:absolute;top:236px;width:1200px;text-align:center;font-family:"Rajdhani",sans-serif;font-size:64px;line-height:62px;color:var(--white)}
.hero-title span{display:block;color:var(--yellow)}
.hero-sub{position:absolute;top:370px;width:1200px;text-align:center;color:var(--white);font-size:16px;letter-spacing:.5px}
.pill{position:absolute;display:flex;align-items:center;gap:14px;border-radius:26px;font-size:18px;font-weight:500}
.hero .pill{left:427px;top:430px;width:346px;height:44px;background:var(--yellow);color:var(--ink);padding-left:26px}
.dot{position:absolute;width:34px;height:34px;border-radius:50%;background:var(--yellow)}

/* solution */
.solution{top:711px;height:489px;background:var(--light)}
.sec-title{text-align:center;font-size:30px;font-weight:500;line-height:42px}
.solution .sec-title{margin-top:52px}
.cards{display:flex;justify-content:space-between;width:900px;margin:36px auto 0}
.card{width:250px;text-align:center;font-size:12px;line-height:20px;color:#333}
.card .art{width:170px;height:150px;margin:0 auto 20px;border-radius:6px;background:linear-gradient(135deg,#fde39a,#f4c63c 60%,#e7eef8)}

/* celebrate */
.celebrate{top:1200px;height:563px;background:var(--white)}
.celebrate-photo{left:0;top:0;width:600px;height:563px;background:linear-gradient(135deg,#d9d7d2,#9c978e 55%,#5a5650)}
.celebrate-copy{position:absolute;left:680px;top:136px;width:440px}
.celebrate-copy h2{font-size:31px;font-weight:500;line-height:42px;margin-bottom:26px}
.arrow-list li{list-style:none;display:flex;gap:20px;font-size:11.5px;line-height:19px;color:var(--muted);margin-bottom:20px}
.arrow-list svg{flex:none;margin-top:2px}

/* team */
.team{top:1763px;height:555px;background:var(--dark);color:var(--white)}
.team h2{position:absolute;left:138px;top:128px;font-size:31px;font-weight:500}
.team-text{position:absolute;left:138px;top:194px;width:420px;font-size:11.5px;line-height:21px}
.team-text p{margin-bottom:14px}
.team-text a{color:var(--yellow)}
.team-badge{position:absolute;left:-40px;top:428px;width:440px;height:240px;border-radius:220px 220px 0 0;background:var(--yellow);color:var(--ink)}
.team-badge strong{position:absolute;left:168px;top:52px;font-size:19px;font-weight:600}
.team-badge em{position:absolute;left:193px;top:80px;font-size:13px;font-weight:600;text-decoration:underline}
.team-deco{position:absolute;left:740px;top:60px;width:420px;height:420px;border:10px solid var(--yellow);transform:rotate(45deg);opacity:.9}
.team-photo{left:690px;top:110px;width:340px;height:445px;border-radius:170px 170px 0 0;background:linear-gradient(180deg,#5b4435,#2f2724 60%,#1f2a4a)}

/* services */
.services{top:2318px;height:2022px;background:var(--white)}
.services .sec-title{margin-top:70px}
.services-intro{width:600px;margin:10px auto 0;text-align:center;font-size:12px;line-height:20px;color:var(--muted)}
.svc{position:absolute;width:1200px;height:450px}
.svc .photo{position:absolute;top:0;width:540px;height:450px}
.svc .copy{position:absolute;top:0;width:540px;height:450px}
.num{font-size:96px;font-weight:500;color:var(--yellow);line-height:96px;height:58px;overflow:hidden;margin-top:38px}
.svc h3{font-size:25px;font-weight:500;line-height:30px;margin:2px 0 24px}
.ticks li{list-style:none;display:flex;gap:14px;font-size:12px;line-height:26px;color:#333}
.ticks li::before{content:"";flex:none;width:8px;height:8px;margin-top:9px;border:2px solid var(--yellow);transform:rotate(45deg)}

/* contact */
.contact{top:4340px;height:677px;background:var(--yellow)}
.contact h2{position:absolute;top:82px;width:1200px;text-align:center;font-size:30px;font-weight:500;line-height:40px}
.contact .lead{position:absolute;top:168px;width:1200px;text-align:center;font-size:14px;color:#7b5b00}
.contact .pill{left:388px;top:226px;width:424px;height:48px;border:1.5px solid var(--ink);padding-left:52px;font-size:20px}
.footer-brand{position:absolute;left:58px;top:580px;font-size:22px;font-weight:500;letter-spacing:1px;color:var(--white);display:flex;align-items:center;gap:10px}
.footer-brand .mark{width:16px;height:16px;background:var(--yellow)}
.social{position:absolute;top:542px;right:58px;display:flex;gap:8px}
.social span{width:36px;height:36px;border:1.5px solid var(--yellow);border-radius:50%;display:flex;align-items:center;justify-content:center}
.social i{width:12px;height:12px;background:var(--yellow);border-radius:2px}
.footer-links{position:absolute;right:58px;top:594px;font-size:11px;color:var(--white)}
.footer-copy{position:absolute;right:58px;top:618px;font-size:11px;color:var(--white)}
</style>
</head>
<body>

<header class="section hero">
  <div class="fill hero-photo" role="img" aria-label="Photo of a woman at a laptop beside a job search screen"></div>
  <div class="fill hero-shade"></div>
  <svg class="hero-shape" width="1200" height="711" viewBox="0 0 1200 711">
    <polygon points="0,572 270,620 300,705 900,705 930,620 1200,560 1200,711 0,711" fill="var(--yellow)"/>
    <polygon points="0,592 255,636 282,711 918,711 945,636 1200,584 1200,711 0,711" fill="var(--white)"/>
    <circle cx="600" cy="665" r="14" fill="var(--yellow)"/>
  </svg>
  <div class="brand"><span class="mark"></span>TALLO HR CONSULTING</div>
  <nav class="nav">
    <span class="active">Home</span><span>Resources Solution</span><span>Business</span><span>Our Team</span><span>Our Services</span><span class="cta">CONTACT US</span>
  </nav>
  <h1 class="hero-title">WE CREATE PERFECT<span>CONNECTIONS</span></h1>
  <p class="hero-sub">We will Help you find the Best Employee for your Projects</p>
  <div class="pill">
    <svg width="28" height="20" viewBox="0 0 28 20"><rect x="1" y="1" width="26" height="18" rx="2" fill="none" stroke="var(--ink)" stroke-width="2"/><path d="M1 2 L14 12 L27 2" fill="none" stroke="var(--ink)" stroke-width="2"/></svg>
    info@tallohrconsulting.com
  </div>
</header>

<section class="section solution">
  <h2 class="sec-title">Your Human Resources<br><span class="accent">Solution</span></h2>
  <div class="cards">
    <div class="card"><div class="art" role="img" aria-label="Illustration of a woman working at a laptop with chat bubbles"></div>HR Tallo Consulting is the solution to all your HR issues. We are a one-stop-shop providing a variety of services</div>
    <div class="card"><div class="art" role="img" aria-label="Illustration of two people talking at a high table"></div>Whether you have a specific HR need or seek relief by outsourcing altogether, we have you covered</div>
    <div class="card"><div class="art" role="img" aria-label="Illustration of a person with a laptop and a dashboard screen"></div>For some clients, an HR Tallo Consultant is known as the HR department and for others, we simply step in as needed on a Project basis</div>
  </div>
</section>

<section class="section celebrate">
  <div class="fill celebrate-photo" role="img" aria-label="Photo of colleagues in a discussion at a meeting table"></div>
  <div class="celebrate-copy">
    <h2>Celebrating <span class="accent">15</span> Years In <span class="accent">Business</span></h2>
    <ul class="arrow-list">
      <li><svg width="44" height="12" viewBox="0 0 44 12"><path d="M0 6 H42 M36 1 L42 6 L36 11" fill="none" stroke="var(--yellow)" stroke-width="1.6"/></svg>For Fifteen Years Our Team Of Industry Experts Has Been Providing HR Consulting Services With Innovative Strategies And A Partnership Mentality</li>
      <li><svg width="44" height="12" viewBox="0 0 44 12"><path d="M0 6 H42 M36 1 L42 6 L36 11" fill="none" stroke="var(--yellow)" stroke-width="1.6"/></svg>We Have Worked With Some Of The Most Innovative Companies In Silicon Valley, Across A Broad Range Of Industries, And We're Proud To Grow Our Client List Every Year</li>
      <li><svg width="44" height="12" viewBox="0 0 44 12"><path d="M0 6 H42 M36 1 L42 6 L36 11" fill="none" stroke="var(--yellow)" stroke-width="1.6"/></svg>HR Tallo's experienced professionals help implement and maintain best practices, allowing our clients to focus on their core competencies.</li>
    </ul>
  </div>
</section>

<section class="section team">
  <h2>Our <span class="accent">Team</span></h2>
  <div class="team-text">
    <p>Our Team Is Woman-owned, Women-led And Partnership-oriented.</p>
    <p>Working With Us Means You're Hiring Senior-level Talent That Acts As An Extension Of Your Company.</p>
    <p>We're Here To Educate Companies And Help Them Solve Complex HR Problems</p>
    <p>Information About Our CEO, Marisa Quell, Can Be <a href="#">Found Here</a></p>
  </div>
  <div class="team-deco"></div>
  <div class="fill team-photo" role="img" aria-label="Portrait photo of the company CEO"></div>
  <div class="team-badge"><strong>Marisa Quell</strong><em>Learn More</em></div>
</section>

<section class="section services">
  <h2 class="sec-title">Our <span class="accent">Services</span></h2>
  <p class="services-intro">We help assess your HR needs and offer ongoing HR Department services or defined projects based on your organization's unique needs and goals</p>

  <div class="svc" style="top:224px">
    <div class="photo" style="left:60px;background:linear-gradient(135deg,#e7e2da,#b9ad9c 60%,#6f6558)" role="img" aria-label="Photo of a woman working on a laptop"></div>
    <div class="copy" style="left:702px">
      <div class="num">01</div><h3>Set Up</h3>
      <ul class="ticks"><li>Select and implement an HRIS system</li><li>Create Company Handbook</li><li>Write termination procedure</li><li>Set up benefits services</li><li>Set up workers comp vendor</li><li>Create job descriptions for current and anticipated roles</li></ul>
    </div>
  </div>

  <div class="svc" style="top:674px">
    <div class="copy" style="left:134px">
      <div class="num">02</div><h3>Managing HR Functions/<br>Recruiting</h3>
      <ul class="ticks"><li>Onboarding/Offboarding</li><li>Employee relations</li><li>Investigations</li><li>Leave administration</li><li>Immigration liaison</li><li>Compensation management</li><li>Full cycle recruitment</li></ul>
    </div>
    <div class="photo" style="left:600px;background:linear-gradient(135deg,#8f8c88,#4e4b48 55%,#d7d4cf)" role="img" aria-label="Photo of a team meeting around a white table"></div>
  </div>

  <div class="svc" style="top:1124px">
    <div class="photo" style="left:60px;background:linear-gradient(135deg,#c9a77c,#8b6a48 50%,#e6ddd2)" role="img" aria-label="Photo of two women shaking hands in an office"></div>
    <div class="copy" style="left:702px">
      <div class="num">03</div><h3>Recurring Procedures</h3>
      <ul class="ticks"><li>Review handbook annually</li><li>Roll out training (required and soft skills training)</li><li>Write offer letters</li><li>Handle employee data and files</li><li>Conduct I-9 audits</li><li>Handle merit and review bonuses</li></ul>
    </div>
  </div>

  <div class="svc" style="top:1574px">
    <div class="copy" style="left:134px">
      <div class="num">04</div><h3>Partner Communications<br>&amp; Projects</h3>
      <ul class="ticks"><li>Manage annual bidding process for benefits review</li><li>Handle workers compensation claims administration</li><li>Manage leave administration between client, employee<br>and vendor(s)</li><li>Handle EDD inquires</li><li>Partner on M&amp;A activity</li></ul>
    </div>
    <div class="photo" style="left:600px;background:linear-gradient(135deg,#7f8a93,#3f4850 55%,#a9b2b8)" role="img" aria-label="Photo of a woman presenting to colleagues in a meeting room"></div>
  </div>
</section>

<footer class="section contact">
  <h2>We Look Forward To Working<br>With You</h2>
  <p class="lead">Contact Us For a Free Consultation</p>
  <div class="pill">
    <svg width="30" height="22" viewBox="0 0 28 20"><rect x="1" y="1" width="26" height="18" rx="2" fill="none" stroke="var(--ink)" stroke-width="2"/><path d="M1 2 L14 12 L27 2" fill="none" stroke="var(--ink)" stroke-width="2"/></svg>
    info@tallohrconsulting.com
  </div>
  <svg class="hero-shape" width="1200" height="677" viewBox="0 0 1200 677">
    <polygon points="0,332 300,382 330,460 870,460 900,382 1200,332 1200,677 0,677" fill="var(--white)"/>
    <polygon points="0,348 290,396 318,474 882,474 910,396 1200,348 1200,677 0,677" fill="var(--darker)"/>
    <circle cx="600" cy="432" r="16" fill="var(--yellow)"/>
  </svg>
  <div class="footer-brand"><span class="mark"></span>TALLO HR CONSULTING</div>
  <div class="social"><span><i></i></span><span><i></i></span><span><i></i></span></div>
  <div class="footer-links">Resources Solution &nbsp;|&nbsp; Business &nbsp;|&nbsp; Our Team &nbsp;|&nbsp; Our Services &nbsp;|&nbsp; Contact Us</div>
  <div class="footer-copy">©HR <span class="accent">TALLO</span> CONSULTING - 2021 All rights reserved.</div>
</footer>

</body>
</html>
```